Garnett and Lyle Personal Injury Billboard

We'd like a clean/modern billboard to build brand awareness for our law firm in the area of personal injury. Ideally, we like the word "Injured?" or something similar in large lettering.

I'm attaching images, logo and award badges which could be used. The billboards will be 14x48 ft and 10.6x36.

We are open to different color ideas, fonts, and artwork. Creative but not too busy with wording. Our web page is www.kgarnettfirm.example

Garnett & Lyle Law Firm
(555) 318-4092

```html
<!DOCTYPE html>
<html lang="en">
<head>
<meta charset="UTF-8">
<title>Garnett &amp; Lyle Law Firm – Billboard</title>
<link rel="stylesheet" href="https://fonts.googleapis.com/css2?family=Montserrat:wght@500;600;700&family=Roboto:wght@700&display=swap">
<style>
  :root {
    --brand-blue: #0262ae;
    --ink: #111111;
    --board-white: #ffffff;
    --backdrop: #e6e9ed;
    --badge-cyan: #1ab3ea;
    --badge-dark: #2b2b2d;
    --badge-sky: #7fd3f3;
    --portrait-light: #c9ccd1;
    --portrait-dark: #5a5f68;
  }
  * { box-sizing: border-box; margin: 0; padding: 0; }
  html, body {
    width: 1058px;
    height: 1200px;
    overflow: hidden;
    background: var(--backdrop);
  }
  .canvas {
    position: relative;
    width: 1058px;
    height: 1200px;
  }
  .billboard {
    position: absolute;
    left: 29px;
    top: 454px;
    width: 1000px;
    height: 292px;
    background: var(--board-white);
    overflow: hidden;
  }
  .brand-band {
    position: absolute;
    left: 0;
    top: 133px;
    width: 100%;
    height: 59px;
    background: var(--brand-blue);
  }
  .firm-name-mark {
    position: absolute;
    left: 48px;
    top: 48px;
    width: 170px;
    font-family: "Montserrat", sans-serif;
    font-weight: 700;
    font-size: 24px;
    line-height: 27px;
    color: var(--ink);
    letter-spacing: 0.5px;
  }
  .headline {
    position: absolute;
    left: 246px;
    top: 30px;
    font-family: "Montserrat", sans-serif;
    font-weight: 600;
    font-size: 99px;
    line-height: 1;
    color: var(--brand-blue);
    letter-spacing: -1px;
  }
  .firm-name {
    position: absolute;
    left: 252px;
    top: 133px;
    height: 59px;
    line-height: 59px;
    font-family: "Montserrat", sans-serif;
    font-weight: 500;
    font-size: 33.5px;
    color: var(--board-white);
    letter-spacing: 1px;
    white-space: nowrap;
  }
  .portrait {
    position: absolute;
    top: 156px;
    width: 94px;
    height: 94px;
    border-radius: 50%;
    border: 2px solid var(--brand-blue);
    background: radial-gradient(circle at 50% 40%, var(--portrait-light) 0 45%, var(--portrait-dark) 100%);
  }
  .portrait--first { left: 35px; }
  .portrait--second { left: 131px; }
  .contact-box {
    position: absolute;
    left: 252px;
    top: 204px;
    width: 496px;
    height: 46px;
    border: 1.5px solid var(--brand-blue);
    display: flex;
    font-family: "Roboto", sans-serif;
    font-weight: 700;
    font-size: 21px;
    color: var(--ink);
    white-space: nowrap;
  }
  .contact-phone {
    width: 208px;
    border-right: 1.5px solid var(--brand-blue);
    display: flex;
    align-items: center;
    justify-content: center;
  }
  .contact-web {
    flex: 1;
    display: flex;
    align-items: center;
    justify-content: center;
  }
  .award-badge {
    position: absolute;
    left: 804px;
    top: 45px;
    width: 146px;
    height: 204px;
  }
</style>
</head>
<body>
  <div class="canvas">
    <section class="billboard">
      <div class="brand-band"></div>

      <div class="firm-name-mark">GARNETT<br>&amp; LYLE</div>

      <h1 class="headline">INJURED?</h1>
      <p class="firm-name">GARNETT &amp; LYLE LAW FIRM</p>

      <div class="portrait portrait--first" role="img" aria-label="Portrait photo of the first attorney"></div>
      <div class="portrait portrait--second" role="img" aria-label="Portrait photo of the second attorney"></div>

      <div class="contact-box">
        <div class="contact-phone">(555) 318-4092</div>
        <div class="contact-web">www.kgarnettfirm.example</div>
      </div>

      <svg class="award-badge" viewBox="0 0 146 204" role="img" aria-label="Community award winner badge">
        <rect x="0" y="0" width="146" height="204" fill="#1ab3ea"/>
        <rect x="4" y="4" width="138" height="170" fill="#2b2b2d"/>
        <rect x="4" y="4" width="138" height="28" fill="#7fd3f3"/>
      </svg>
    </section>
  </div>
</body>
</html>
```